Ferncrest Dental, LLC business card project

Business card to be designed with current logo.
Dental office- please keep design of card that looks clean and professional.
Please include the following info:
Ferncrest Dental, LLC
Dr. Lorna Pettigrew
2871 Marlowe Street
Bethlehem, PA 18093
610-555-0193
ferncrestdental.office@examplemail.test
Hello everyone-
Reason: Just got back from overseas- will look at all designs and provide feedback. Thank you!
Reason: Polling my friends for the final selection-
thank you to all those that participated- so many talented designers!

```html
<!DOCTYPE html>
<html lang="en">
<head>
<meta charset="utf-8">
<title>Ferncrest Dental, LLC — Business Card</title>
<link rel="stylesheet" href="https://fonts.googleapis.com/css2?family=Marcellus&display=swap">
<style>
  :root {
    --card-bg: #ffffff;
    --brand-green: #6fa83c;
    --text-green: #8cc13f;
    --rule-green: #a9cb3c;
    --mark-green: #b5d65a;
    --band-green: #5f9a35;
    --band-text: #d3e877;
  }
  * { margin: 0; padding: 0; box-sizing: border-box; }
  html, body {
    width: 1200px;
    height: 638px;
    overflow: hidden;
    background: var(--card-bg);
  }
  .card {
    position: relative;
    width: 1200px;
    height: 638px;
    background: var(--card-bg);
    font-family: "Marcellus", Georgia, serif;
    color: var(--text-green);
  }
  .brand {
    position: absolute;
    left: 70px;
    top: 18px;
    display: flex;
    align-items: center;
    gap: 28px;
  }
  .brand-dot {
    width: 86px;
    height: 86px;
    border-radius: 50%;
    background: var(--mark-green);
  }
  .brand-name {
    font-size: 84px;
    line-height: 1;
    color: var(--brand-green);
    white-space: nowrap;
  }
  .doctor {
    position: absolute;
    left: 115px;
    top: 196px;
    font-size: 42px;
    line-height: 1;
  }
  .divider {
    position: absolute;
    left: 598px;
    top: 165px;
    width: 4px;
    height: 322px;
    background: var(--rule-green);
  }
  .address {
    position: absolute;
    left: 650px;
    width: 470px;
    top: 200px;
    text-align: center;
    font-size: 31px;
    line-height: 44px;
    font-style: normal;
  }
  .phone {
    position: absolute;
    left: 650px;
    width: 470px;
    top: 386px;
    text-align: center;
    font-size: 38px;
    line-height: 1;
  }
  .contact-band {
    position: absolute;
    left: 0;
    bottom: 0;
    width: 1200px;
    height: 131px;
    background: var(--band-green);
    display: flex;
    align-items: center;
    justify-content: center;
  }
  .email {
    font-size: 37px;
    color: var(--band-text);
    white-space: nowrap;
  }
</style>
</head>
<body>
  <div class="card">
    <div class="brand">
      <span class="brand-dot" aria-hidden="true"></span>
      <span class="brand-name">Ferncrest Dental, LLC</span>
    </div>

    <p class="doctor">Dr. Lorna Pettigrew</p>

    <div class="divider" aria-hidden="true"></div>

    <address class="address">
      2871 Marlowe Street<br>
      Bethlehem, PA 18093
    </address>

    <p class="phone">610-555-0193</p>

    <div class="contact-band">
      <p class="email">email: ferncrestdental.office@examplemail.test</p>
    </div>
  </div>
</body>
</html>
```